Business Card Design - Lumo Fitters

Lumo Fitters is a service company which carried out installation and maintenance work in the GPS Tracking industry.

We install and maintain GPS Tracking hardware into cars, trucks etc.

We have an existing design with existing logo which I would like to improve on. I would like to be able to edit the design in the future when we have new staff come on board. We currently have 8 or so different employees who would all require cards - ideally I need to be able to edit a template in photoshop or something.

The back of the existing design has a white outline of Australia with a white dot over: Brisbane, Sydney, Melbourne, Adelaide and Perth.

Our current cards are mainly black, our uniforms are black - happy to look at changing that if the look is right.

We strive to be organised, professional and we are working in the technology sector.

Cheers.

Industry/Entity Type

Business

Contact Information for Business Card

Name
Mobile number
Email address
Web address

Requirements
Must have
• Map of Australia as mentioned above.

```html
<!DOCTYPE html>
<html lang="en">
<head>
<meta charset="utf-8">
<title>Lumo Fitters – Business Cards</title>
<link href="https://fonts.googleapis.com/css2?family=Questrial&display=swap" rel="stylesheet">
<style>
  :root {
    --navy: #282a79;
    --white: #ffffff;
    --swoosh: rgba(255, 255, 255, 0.28);
    --map-tone: #3a3f8c;
    --sheet-top: #d9dadc;
    --sheet-mid: #f4f4f5;
    --sheet-bottom: #dcdddf;
  }
  * { box-sizing: border-box; margin: 0; padding: 0; }
  html, body {
    width: 1200px;
    height: 1000px;
    overflow: hidden;
  }
  body {
    position: relative;
    background: linear-gradient(180deg, var(--sheet-top) 0%, var(--sheet-mid) 55%, var(--sheet-bottom) 100%);
    font-family: "Questrial", sans-serif;
    color: var(--white);
  }
  .card {
    position: absolute;
    width: 511px;
    height: 315px;
    background: var(--navy);
    overflow: hidden;
  }
  .card--marcus-front { left: 37px;  top: 26px; }
  .card--marcus-back  { left: 37px;  top: 359px; }
  .card--owen-front   { left: 635px; top: 299px; }
  .card--owen-back    { left: 635px; top: 632px; }

  .swoosh {
    position: absolute;
    left: 0; top: 0;
    width: 511px; height: 315px;
  }
  .brand-name {
    position: absolute;
    top: 58px;
    width: 100%;
    text-align: center;
    font-size: 50px;
    line-height: 1;
    letter-spacing: 1px;
    color: var(--white);
  }
  .card--marcus-front .brand-name { left: 5px; }
  .card--owen-front .brand-name { left: -14px; }

  .contact {
    position: absolute;
    left: 40px;
    top: 186px;
    letter-spacing: 1.6px;
  }
  .contact__name {
    font-size: 18px;
    margin-bottom: 13px;
  }
  .contact__line {
    font-size: 17px;
    line-height: 23.5px;
  }
  .contact__line--indent { padding-left: 6px; }

  .map-area {
    position: absolute;
    top: 36px;
    width: 305px;
    height: 238px;
    background: var(--map-tone);
    border-radius: 6px;
  }
  .card--marcus-back .map-area { left: 90px; }
  .card--owen-back .map-area { left: 76px; }
</style>
</head>
<body>

  <section class="card card--marcus-front">
    <svg class="swoosh" viewBox="0 0 511 315" aria-hidden="true">
      <path d="M190 212 C290 196 330 262 400 258 C450 255 480 228 511 218 L511 238 C478 246 450 272 398 272 C330 274 290 214 190 212 Z" fill="var(--swoosh)"/>
    </svg>
    <div class="brand-name">Lumo Fitters</div>
    <div class="contact">
      <div class="contact__name">MARCUS DELANE</div>
      <div class="contact__line contact__line--indent">T : 0400 555 218</div>
      <div class="contact__line contact__line--indent">E : marcus@lumofitters.com.au</div>
      <div class="contact__line">W : www.lumofitters.com.au</div>
    </div>
  </section>

  <section class="card card--marcus-back">
    <div class="map-area" role="img" aria-label="Outline map of Australia with dots marking Perth, Adelaide, Melbourne, Sydney and Brisbane"></div>
  </section>

  <section class="card card--owen-front">
    <svg class="swoosh" viewBox="0 0 511 315" aria-hidden="true">
      <path d="M0 222 C60 232 110 262 180 246 C260 226 300 190 370 190 C410 190 445 202 468 214 C440 206 410 200 372 204 C300 212 260 252 180 262 C110 270 60 246 0 240 Z" fill="var(--swoosh)"/>
    </svg>
    <div class="brand-name">Lumo Fitters</div>
    <div class="contact">
      <div class="contact__name">OWEN RACKLEY</div>
      <div class="contact__line contact__line--indent">T : 0400 555 764</div>
      <div class="contact__line contact__line--indent">E : owen@lumofitters.com.au</div>
      <div class="contact__line">W : www.lumofitters.com.au</div>
    </div>
  </section>

  <section class="card card--owen-back">
    <div class="map-area" role="img" aria-label="Outline map of Australia with dots marking Perth, Adelaide, Melbourne, Sydney and Brisbane"></div>
  </section>

</body>
</html>
```